Australia's newest tech recruitment startup

We are a new tech startup in the recruitment space.

We leverage the existing infrastructure of the recruitment network and bundle a value market based business model (like brisk fennel) that appeals to business.

We are very individual, afraid of no one, minimalist, and defiantly NO "BS"!!

We're not cut price think Vantor Hale rather than Kesumi
Updates

Hey Everyone,

thanks so much for your designs. I have eliminated a lot of designs but if I havent to yours then your in with a shot. I would like to see the designs updated with a spot for our twitter handle, my blog address & our linkedIn group address. 

For some designs I think some of the above would look ok on the back of the card so not to make the front look too messy. 

thanks   

Target Market(s)

Our target market is SME's young baby boomer and Gen X

Industry/Entity Type

Business

Requirements
Must have
• Company logo, doesn't have to be both

```html
<!DOCTYPE html>
<html lang="en">
<head>
<meta charset="utf-8">
<title>LinkHire – Business Card</title>
<link href="https://fonts.googleapis.com/css2?family=Tenor+Sans&display=swap" rel="stylesheet">
<style>
  :root {
    --page-bg: #ececec;
    --card-white: #ffffff;
    --brand-blue: #17aee6;
    --text-font: "Tenor Sans", "Gill Sans", sans-serif;
  }
  * { margin: 0; padding: 0; box-sizing: border-box; }
  html, body {
    width: 1200px; height: 1000px; overflow: hidden;
    background: var(--page-bg);
  }
  .canvas { position: relative; width: 1200px; height: 1000px; }
  .business-card {
    position: absolute; left: 392px; top: 128px;
    width: 428px; height: 722px;
    background: var(--card-white);
    box-shadow: 1px 3px 6px rgba(0,0,0,0.22);
    font-family: var(--text-font);
    color: var(--brand-blue);
  }
  .brand-panel {
    position: absolute; left: 0; top: 0; width: 100%; height: 382px;
    background: var(--brand-blue);
    display: flex; align-items: center; justify-content: center;
  }
  .brand-name {
    color: var(--card-white);
    font-family: var(--text-font);
    font-size: 52px; letter-spacing: 1px;
    margin-top: 8px;
  }
  .person {
    position: absolute; left: 52px; top: 448px;
    text-transform: uppercase;
  }
  .person-name { font-size: 27px; letter-spacing: 2.6px; line-height: 32px; }
  .person-role { font-size: 16px; letter-spacing: 3.2px; line-height: 22px; }
  .contact-list {
    position: absolute; left: 52px; top: 534px;
    list-style: none; text-transform: uppercase;
    font-size: 15px; letter-spacing: 1.1px;
  }
  .contact-item {
    display: flex; align-items: center; height: 32px;
  }
  .contact-icon { width: 18px; height: 18px; margin-right: 16px; flex: none; }
</style>
</head>
<body>
<div class="canvas">
  <div class="business-card">
    <div class="brand-panel">
      <span class="brand-name">LinkHire</span>
    </div>

    <div class="person">
      <div class="person-name">Tom Wells</div>
      <div class="person-role">Consultant</div>
    </div>

    <ul class="contact-list">
      <li class="contact-item">
        <svg class="contact-icon" viewBox="0 0 18 18" aria-hidden="true">
          <path d="M9 1.2a5.6 5.6 0 0 0-5.6 5.6c0 4 5.6 10.2 5.6 10.2s5.6-6.2 5.6-10.2A5.6 5.6 0 0 0 9 1.2z" fill="none" stroke="var(--brand-blue)" stroke-width="1.8"/>
          <circle cx="9" cy="6.8" r="2" fill="var(--brand-blue)"/>
        </svg>
        118 Harlow Street
      </li>
      <li class="contact-item">
        <svg class="contact-icon" viewBox="0 0 18 18" aria-hidden="true">
          <rect x="1.5" y="4" width="15" height="10" fill="none" stroke="var(--brand-blue)" stroke-width="1.8"/>
          <path d="M1.5 4.5 9 10l7.5-5.5" fill="none" stroke="var(--brand-blue)" stroke-width="1.8"/>
        </svg>
        tom@linkhire.com.au
      </li>
      <li class="contact-item">
        <svg class="contact-icon" viewBox="0 0 18 18" aria-hidden="true">
          <path d="M4.2 1.8 6.6 4.6 5.2 6.6c.9 2.2 2.8 4.2 5.2 5.4l1.9-1.5 2.9 2.3-1.7 2.5C8 14.9 3 9.8 2 3.5z" fill="none" stroke="var(--brand-blue)" stroke-width="1.5" stroke-linejoin="round"/>
        </svg>
        +61 0 3518 0000
      </li>
      <li class="contact-item">
        <svg class="contact-icon" viewBox="0 0 18 18" aria-hidden="true">
          <circle cx="9" cy="9" r="7" fill="var(--brand-blue)"/>
        </svg>
        @linkhire
      </li>
    </ul>
  </div>
</div>
</body>
</html>
```